Indian Lunch Delivery company needs a google ad banner for advertising its offering

We are a Kolkata, India based startup delivering lunch to office buildings in the city. We only serve set meals (vegetarian and non-vegetarian). Minimum order quantity is 5 boxes. The name of the brand is Brimvora (Thali=platter). Our USP-
We cook fresh
Trans-fat free
No emulsifiers, preservatives or artificial colorings used.
Importantly, we are a value for money brand. To be precise our meals costs just .99 c.
Target Market(s)
Young professionals
Industry/Entity Type
It Company
Font styles to use
Sans Serif
Requirements
Must have
- Home made food feel to it
Nice to have
- Lots of colours

```html
<!DOCTYPE html>
<html lang="en">
<head>
<meta charset="utf-8">
<title>Brimvora – Set Meal Banners</title>
<link rel="stylesheet" href="https://fonts.googleapis.com/css2?family=Open+Sans:wght@400;600;700;800&display=swap">
<style>
  :root {
    --page: #e1e2e4;
    --orange: #e07808;
    --maroon: #640a04;
    --maroon-deep: #3e0603;
    --gold: #d9a300;
    --cream: #ffd779;
    --white: #ffffff;
    --button: #5a0c06;
    --logo-grey: #8a8b8f;
  }
  * { box-sizing: border-box; margin: 0; padding: 0; }
  html, body { width: 1200px; height: 1152px; overflow: hidden; background: var(--page); }
  body { font-family: "Open Sans", Arial, sans-serif; }
  .stage { position: relative; width: 1000px; height: 960px; transform: scale(1.2); transform-origin: 0 0; }
  .banner { position: absolute; overflow: hidden; background: var(--orange); color: var(--white); }
  .banner svg.art { position: absolute; inset: 0; }
  .banner--skyscraper { left: 371px; top: 117px; width: 240px; height: 400px; }
  .banner--leaderboard { left: 35px; top: 595px; width: 930px; height: 180px; }
  .copy { position: absolute; }
  .headline { font-weight: 700; text-shadow: 0 1px 2px rgba(80,20,0,.45); letter-spacing: -.2px; white-space: nowrap; }
  .subline { color: #ffe1b0; font-weight: 400; }
  .minimum { font-weight: 700; }
  .usp-list { list-style: none; color: var(--cream); }
  .usp-list li { position: relative; padding-left: 19px; line-height: 1.35; }
  .usp-list svg { position: absolute; left: 0; top: 2px; width: 11px; height: 11px; }
  .order-button {
    position: absolute; display: flex; align-items: center; justify-content: center; gap: 8px;
    background: var(--button); border-radius: 5px; color: var(--white); font-weight: 700;
    box-shadow: 0 2px 3px rgba(60,10,0,.45);
  }
  .order-button svg { width: 8px; height: 10px; }
  .brand-badge {
    position: absolute; border-radius: 50%; background: var(--logo-grey); border-style: solid; border-color: var(--gold);
    display: flex; align-items: center; justify-content: center; color: var(--white); font-weight: 700;
  }

  .banner--skyscraper .copy { left: 10px; top: 197px; width: 225px; }
  .banner--skyscraper .headline { font-size: 15.5px; }
  .banner--skyscraper .subline { font-size: 11.5px; margin-top: -3px; }
  .banner--skyscraper .minimum { font-size: 11.5px; margin-top: 6px; }
  .banner--skyscraper .usp-list { font-size: 11.5px; margin-top: 8px; }
  .banner--skyscraper .usp-list li { margin-bottom: 4px; }
  .banner--skyscraper .order-button { left: 33px; top: 351px; width: 122px; height: 28px; font-size: 13.5px; }
  .banner--skyscraper .brand-badge { left: 175px; top: 328px; width: 55px; height: 55px; border-width: 3px; font-size: 7.5px; }

  .banner--leaderboard .copy { left: 468px; top: 12px; width: 340px; }
  .banner--leaderboard .headline { font-size: 21px; }
  .banner--leaderboard .subline { font-size: 14px; margin-top: -4px; }
  .banner--leaderboard .minimum { font-size: 16px; margin-top: 8px; }
  .banner--leaderboard .usp-columns { display: flex; gap: 22px; margin-top: 8px; }
  .banner--leaderboard .usp-list { font-size: 13px; }
  .banner--leaderboard .usp-list li { margin-bottom: 2px; }
  .banner--leaderboard .order-button { left: 543px; top: 143px; width: 122px; height: 28px; font-size: 14px; }
  .banner--leaderboard .brand-badge { left: 792px; top: 9px; width: 126px; height: 126px; border-width: 6px; font-size: 15px; }
</style>
</head>
<body>
<div class="stage">

  <!-- Vertical skyscraper banner -->
  <section class="banner banner--skyscraper">
    <svg class="art" viewBox="0 0 240 400" width="240" height="400">
      <defs>
        <linearGradient id="meal-tall" x1="0" y1="0" x2="1" y2="1">
          <stop offset="0" stop-color="#c9b79a"/>
          <stop offset=".45" stop-color="#b5562a"/>
          <stop offset="1" stop-color="#5c1a08"/>
        </linearGradient>
      </defs>
      <path d="M0 0 H240 V140 Q150 160 70 185 Q30 193 0 186 Z" fill="var(--maroon)"/>
      <path d="M0 0 H240 V122 Q140 150 60 180 Q25 190 0 178 Z" fill="url(#meal-tall)" role="img" aria-label="Photo of an Indian set meal with rice, curry, naan and salad"/>
      <path d="M0 176 Q30 192 70 180 Q150 150 240 125" fill="none" stroke="var(--gold)" stroke-width="5"/>
      <path d="M120 400 Q200 398 240 370 V400 Z" fill="var(--gold)"/>
      <path d="M130 400 Q205 397 240 378 V400 Z" fill="var(--maroon)"/>
    </svg>
    <div class="copy">
      <h1 class="headline">WE ONLY SERVE SET MEALS</h1>
      <p class="subline">(vegetarian and non-vegetarian)</p>
      <p class="minimum">Minimum order quantity is 5 boxes.</p>
      <ul class="usp-list">
        <li><svg viewBox="0 0 12 12"><rect x="1" y="2" width="9" height="9" fill="none" stroke="currentColor" stroke-width="1.2"/><path d="M3 6 L5.5 8.5 L11 1.5" fill="none" stroke="currentColor" stroke-width="1.6"/></svg>We cook fresh</li>
        <li><svg viewBox="0 0 12 12"><rect x="1" y="2" width="9" height="9" fill="none" stroke="currentColor" stroke-width="1.2"/><path d="M3 6 L5.5 8.5 L11 1.5" fill="none" stroke="currentColor" stroke-width="1.6"/></svg>Trans-fat free</li>
        <li><svg viewBox="0 0 12 12"><rect x="1" y="2" width="9" height="9" fill="none" stroke="currentColor" stroke-width="1.2"/><path d="M3 6 L5.5 8.5 L11 1.5" fill="none" stroke="currentColor" stroke-width="1.6"/></svg>No emulsifiers, preservatives<br>or artificial colorings used.</li>
      </ul>
    </div>
    <a class="order-button">ORDER NOW <svg viewBox="0 0 8 10"><path d="M0 0 L8 5 L0 10 Z" fill="var(--gold)"/></svg></a>
    <div class="brand-badge">BRIMVORA</div>
  </section>

  <!-- Horizontal leaderboard banner -->
  <section class="banner banner--leaderboard">
    <svg class="art" viewBox="0 0 930 180" width="930" height="180">
      <defs>
        <linearGradient id="meal-wide" x1="0" y1="0" x2="1" y2="0">
          <stop offset="0" stop-color="#d8ccb4"/>
          <stop offset=".35" stop-color="#b85a2c"/>
          <stop offset=".7" stop-color="#8a2a0c"/>
          <stop offset="1" stop-color="#5a1206"/>
        </linearGradient>
      </defs>
      <path d="M0 0 H458 Q440 125 300 180 H0 Z" fill="var(--maroon)"/>
      <path d="M0 0 H420 Q400 120 280 180 H0 Z" fill="url(#meal-wide)" role="img" aria-label="Photo of an Indian thali with rice and peas, curry, naan, salad and a bowl of spiced dish"/>
      <path d="M458 0 Q440 125 300 180" fill="none" stroke="var(--gold)" stroke-width="5"/>
      <path d="M700 180 Q860 178 930 100 V180 Z" fill="var(--gold)"/>
      <path d="M720 180 Q870 178 930 115 V180 Z" fill="var(--maroon)"/>
    </svg>
    <div class="copy">
      <h1 class="headline">WE ONLY SERVE SET MEALS.</h1>
      <p class="subline">(vegetarian and non-vegetarian)</p>
      <p class="minimum">Minimum order quantity is 5 boxes.</p>
      <div class="usp-columns">
        <ul class="usp-list">
          <li><svg viewBox="0 0 12 12"><rect x="1" y="2" width="9" height="9" fill="none" stroke="currentColor" stroke-width="1.2"/><path d="M3 6 L5.5 8.5 L11 1.5" fill="none" stroke="currentColor" stroke-width="1.6"/></svg>We cook fresh</li>
          <li><svg viewBox="0 0 12 12"><rect x="1" y="2" width="9" height="9" fill="none" stroke="currentColor" stroke-width="1.2"/><path d="M3 6 L5.5 8.5 L11 1.5" fill="none" stroke="currentColor" stroke-width="1.6"/></svg>Trans-fat free</li>
        </ul>
        <ul class="usp-list">
          <li><svg viewBox="0 0 12 12"><rect x="1" y="2" width="9" height="9" fill="none" stroke="currentColor" stroke-width="1.2"/><path d="M3 6 L5.5 8.5 L11 1.5" fill="none" stroke="currentColor" stroke-width="1.6"/></svg>No emulsifiers, preservatives<br>or artificial colorings used.</li>
        </ul>
      </div>
    </div>
    <a class="order-button">ORDER NOW <svg viewBox="0 0 8 10"><path d="M0 0 L8 5 L0 10 Z" fill="var(--gold)"/></svg></a>
    <div class="brand-badge">BRIMVORA</div>
  </section>

</div>
</body>
</html>
```